FRONT BUS CARD:

We were maybe thinking to have the text in a "common seal" which is an oval shape. Or CROWN VAULT underlined, then AUSTRALIA underneath...

Picture to have in the seal, or next to the words if seal not used: Gold Bars (3 of them), or scales of justice..

LOGO and pic and font to be in shiny gold.
We want 1 black background design and 1 white background design.

CROWN VAULT TRADERS

```html
<!DOCTYPE html>
<html lang="en">
<head>
<meta charset="utf-8">
<title>Crown Vault Traders – Business Card Options</title>
<link href="https://fonts.googleapis.com/css2?family=Archivo+Black&family=Source+Sans+3:wght@400&display=swap" rel="stylesheet">
<style>
  :root {
    --canvas: #ffffff;
    --label-grey: #a9a9a9;
    --gold-band: #bc9c2a;
    --gold-text: #d9a82a;
    --gold-bright: #f0c42e;
    --gold-light: #f6dc8a;
    --card-white: #ffffff;
    --card-black: #000000;
    --card-edge: #9a9a9a;
    --text-white: #ffffff;
  }
  * { box-sizing: border-box; margin: 0; padding: 0; }
  html, body { width: 1200px; height: 900px; overflow: hidden; background: var(--canvas); }
  body { position: relative; font-family: "Source Sans 3", "Myriad Pro", sans-serif; }

  .option-label {
    position: absolute; top: 122px;
    font-family: "Archivo Black", "Arial Black", sans-serif;
    font-size: 25px; letter-spacing: 3px; color: var(--label-grey);
  }
  .option-label--one { left: 134px; }
  .option-label--two { left: 647px; }

  .card {
    position: absolute; width: 433px; height: 247px; overflow: hidden;
    box-shadow: 1px 1px 1px var(--card-edge), -0.5px -0.5px 0 #d6d6d6;
  }
  .card--white { background: var(--card-white); }
  .card--black { background: var(--card-black); }
  .card--front-one { left: 134px; top: 161px; }
  .card--front-two { left: 643px; top: 161px; }
  .card--back-one { left: 134px; top: 442px; }
  .card--back-two { left: 643px; top: 442px; }

  .info-band { position: absolute; left: 0; top: 158px; width: 100%; height: 76px; background: var(--gold-band); }
  .edge-band { position: absolute; left: 0; width: 100%; height: 16px; background: var(--gold-band); }
  .edge-band--top { top: 0; }
  .edge-band--bottom { bottom: 0; }

  .seal { position: absolute; display: flex; flex-direction: column; align-items: center; }
  .seal__disc { border-radius: 50%; background: radial-gradient(circle at 40% 35%, var(--gold-light), var(--gold-text) 70%); }
  .seal__name { color: var(--gold-text); white-space: nowrap; }
  .card--black .seal__name { color: var(--gold-bright); }
  .seal--small { left: 36px; top: 40px; width: 92px; }
  .seal--small .seal__disc { width: 62px; height: 62px; }
  .seal--small .seal__name { font-size: 12px; margin-top: 6px; }
  .seal--large { left: 0; top: 52px; width: 100%; }
  .seal--large .seal__disc { width: 112px; height: 112px; }
  .seal--large .seal__name { font-size: 17px; margin-top: 8px; }

  .wordmark-rules { position: absolute; left: 160px; top: 16px; }
  .wordmark { position: absolute; left: 174px; top: 27px; width: 200px; text-align: center; }
  .wordmark__name { font-size: 19px; color: var(--gold-text); text-decoration: underline; text-decoration-thickness: 1px; text-underline-offset: 2px; line-height: 1.1; }
  .wordmark__region { font-size: 12px; color: var(--gold-text); text-align: right; padding-right: 25px; line-height: 1.2; }
  .card--black .wordmark__name, .card--black .wordmark__region { color: var(--gold-bright); }
  .card--black .wordmark { top: 34px; }

  .contact { position: absolute; left: 208px; top: 135px; list-style: none; }
  .contact__item { display: flex; align-items: center; height: 16.5px; font-size: 13px; color: var(--text-white); }
  .contact__item--name { height: 24px; margin-bottom: 4px; font-size: 15px; color: var(--gold-text); }
  .card--black .contact__item--name { color: var(--gold-bright); }
  .contact__icon { width: 10px; height: 10px; margin-right: 12px; flex: none; }
</style>
</head>
<body>
  <h2 class="option-label option-label--one">OPTION 1</h2>
  <h2 class="option-label option-label--two">OPTION 2</h2>

  <svg width="0" height="0" style="position:absolute">
    <defs>
      <linearGradient id="rule-gold" x1="0" x2="1">
        <stop offset="0" stop-color="#d9a82a" stop-opacity="0"/>
        <stop offset="0.5" stop-color="#e9c24a"/>
        <stop offset="1" stop-color="#d9a82a" stop-opacity="0"/>
      </linearGradient>
    </defs>
  </svg>

  <!-- Front, white -->
  <section class="card card--white card--front-one">
    <div class="seal seal--small">
      <div class="seal__disc"></div>
      <span class="seal__name">CROWN VAULT</span>
    </div>
    <svg class="wordmark-rules" width="250" height="60">
      <rect x="0" y="2" width="250" height="2" fill="url(#rule-gold)"/>
      <rect x="0" y="55" width="250" height="2" fill="url(#rule-gold)"/>
    </svg>
    <div class="wordmark">
      <div class="wordmark__name">CROWN VAULT</div>
      <div class="wordmark__region">AUSTRALIA</div>
    </div>
    <div class="info-band"></div>
    <ul class="contact">
      <li class="contact__item contact__item--name"><svg class="contact__icon" viewBox="0 0 10 10"><circle cx="5" cy="3" r="2.3" fill="#d9a82a"/><path d="M1 10 Q5 4 9 10Z" fill="#d9a82a"/></svg>your name</li>
      <li class="contact__item"><svg class="contact__icon" viewBox="0 0 10 10"><path d="M1 5 L5 1 L9 5 H8 V9 H2 V5Z" fill="#fff"/></svg>your address</li>
      <li class="contact__item"><svg class="contact__icon" viewBox="0 0 10 10"><path d="M1 3 Q5 0 9 3 L7 5 L6 4 H4 L3 5Z" fill="#fff"/></svg>T:P</li>
      <li class="contact__item"><svg class="contact__icon" viewBox="0 0 10 10"><rect x="3" y="1" width="4" height="8" rx="1" fill="#fff"/></svg>M:P</li>
      <li class="contact__item"><svg class="contact__icon" viewBox="0 0 10 10"><rect x="1" y="2" width="8" height="6" fill="#fff"/></svg>E.mail</li>
    </ul>
  </section>

  <!-- Front, black -->
  <section class="card card--black card--front-two">
    <div class="seal seal--small">
      <div class="seal__disc"></div>
      <span class="seal__name">CROWN VAULT</span>
    </div>
    <svg class="wordmark-rules" width="250" height="80">
      <rect x="0" y="11" width="250" height="2" fill="url(#rule-gold)"/>
      <rect x="0" y="61" width="250" height="2" fill="url(#rule-gold)"/>
    </svg>
    <div class="wordmark">
      <div class="wordmark__name">CROWN VAULT</div>
      <div class="wordmark__region">AUSTRALIA</div>
    </div>
    <div class="info-band"></div>
    <ul class="contact">
      <li class="contact__item contact__item--name"><svg class="contact__icon" viewBox="0 0 10 10"><circle cx="5" cy="3" r="2.3" fill="#f0c42e"/><path d="M1 10 Q5 4 9 10Z" fill="#f0c42e"/></svg>your name</li>
      <li class="contact__item"><svg class="contact__icon" viewBox="0 0 10 10"><path d="M1 5 L5 1 L9 5 H8 V9 H2 V5Z" fill="#fff"/></svg>your address</li>
      <li class="contact__item"><svg class="contact__icon" viewBox="0 0 10 10"><path d="M1 3 Q5 0 9 3 L7 5 L6 4 H4 L3 5Z" fill="#fff"/></svg>T:P</li>
      <li class="contact__item"><svg class="contact__icon" viewBox="0 0 10 10"><rect x="3" y="1" width="4" height="8" rx="1" fill="#fff"/></svg>M:P</li>
      <li class="contact__item"><svg class="contact__icon" viewBox="0 0 10 10"><rect x="1" y="2" width="8" height="6" fill="#fff"/></svg>E.mail</li>
    </ul>
  </section>

  <!-- Back, white -->
  <section class="card card--white card--back-one">
    <div class="edge-band edge-band--top"></div>
    <div class="seal seal--large">
      <div class="seal__disc"></div>
      <span class="seal__name">CROWN VAULT</span>
    </div>
    <div class="edge-band edge-band--bottom"></div>
  </section>

  <!-- Back, black -->
  <section class="card card--black card--back-two">
    <div class="edge-band edge-band--top"></div>
    <div class="seal seal--large">
      <div class="seal__disc"></div>
      <span class="seal__name">CROWN VAULT</span>
    </div>
    <div class="edge-band edge-band--bottom"></div>
  </section>
</body>
</html>
```